Family Ranch with a hobby vineyard needs 2 wine labels for our first harvest

Design 2 wine labels (front and back) with the Brindor Ranch logo.
Label 1:
Sauvignon Blanc
Alc. 12.5% by Vol.
Palos Verdes Peninsula - add as the region
Year 2022
Label 2:
Cabernet Sauvignon
Alc. 13.5% by Vol.
Year 2022
For the back label design:
GOVERNMENT WARNING: (1) According to the Surgeon General, women
should not drink alcoholic beverages during pregnancy because of the risk of
birth defects. (2) Consumption of alcoholic beverages impairs your ability to
drive a car or operate machinery, and may cause health problems.
Contains Sulfates.
750ML
I just received the bottles and have attached a picture.
Look and feel
Each slider illustrates characteristics of the customer's brand and the style your logo design should communicate.

```html
<!DOCTYPE html>
<html lang="en">
<head>
<meta charset="utf-8">
<title>Brindor Ranch – 2022 Wine Labels</title>
<link href="https://fonts.googleapis.com/css2?family=Cinzel:wght@500;700&family=Great+Vibes&family=Tinos&family=Roboto+Condensed:wght@300;700&display=swap" rel="stylesheet">
<style>
  :root{
    --gold:#d3ab46;
    --silver:#c3c3c8;
    --ink:#111111;
    --band-text-gold:#e0b94e;
    --band-text-silver:#ffffff;
    --page:#ffffff;
  }
  *{box-sizing:border-box;margin:0;padding:0}
  html,body{width:1200px;height:939px;overflow:hidden;background:var(--page)}
  .sheet{
    width:1200px;height:939px;
    display:grid;
    grid-template-columns:420px 420px;
    grid-template-rows:420px 420px;
    gap:40px 80px;
    justify-content:center;align-content:center;
  }
  .label{width:420px;height:420px;color:var(--ink);position:relative}
  .label--gold{--face:var(--gold);--band-text:var(--band-text-gold)}
  .label--silver{--face:var(--silver);--band-text:var(--band-text-silver)}

  /* front label */
  .front{background:var(--ink);padding:15px}
  .front__face{background:var(--face);height:100%;padding:11px;position:relative}
  .front__rule{border:1px solid var(--ink);height:100%;display:flex;flex-direction:column;align-items:center;padding-top:44px}
  .brand{display:flex;flex-direction:column;align-items:center}
  .brand__dot{width:74px;height:74px;border-radius:50%;background:var(--ink);margin-bottom:14px}
  .brand__name{font-family:'Cinzel',serif;font-weight:700;font-size:34px;letter-spacing:1px;line-height:1.05;text-align:center}
  .vineyard{font-family:'Great Vibes',cursive;font-size:24px;margin-top:24px;line-height:1}
  .vintage{font-family:'Tinos',serif;font-size:16px;margin-top:4px}
  .variety{font-family:'Cinzel',serif;font-weight:500;font-size:21px;letter-spacing:.5px;line-height:1.2}
  .appellation{font-family:'Tinos',serif;font-size:16px}
  .front__band{position:absolute;left:11px;right:11px;bottom:11px;height:21px;background:var(--ink);
    color:var(--band-text);font-family:'Cinzel',serif;font-size:12px;display:flex;align-items:center;justify-content:center;letter-spacing:.3px}

  /* back label */
  .back{background:var(--face);padding:14px 16px 10px}
  .back__head{display:flex;justify-content:space-between;align-items:flex-start}
  .back__title{width:230px;text-align:center}
  .back__title .vineyard{margin-top:0;font-size:21px}
  .back__title .vintage{font-size:15px;margin-top:2px}
  .back__title .variety{font-size:19px}
  .back__title .appellation{font-size:15px}
  .back__brand{width:150px;margin-top:6px}
  .back__brand .brand__dot{width:46px;height:46px;margin-bottom:8px}
  .back__brand .brand__name{font-size:20px}
  .story{font-family:'Tinos',serif;font-size:11.6px;line-height:1.26;text-align:justify;text-align-last:center;margin-top:12px}
  .story p + p{margin-top:0}
  .stars{text-align:center;font-size:11px;letter-spacing:3px;margin:6px 0 8px}
  .producer{font-family:'Tinos',serif;font-size:11.5px;letter-spacing:.6px;text-align:center}
  .warning{font-family:'Roboto Condensed',sans-serif;font-weight:300;font-size:10.4px;line-height:1.3;text-align:justify;margin-top:8px;text-transform:uppercase}
  .warning strong{font-weight:700}
  .facts{display:flex;justify-content:space-between;font-family:'Roboto Condensed',sans-serif;font-weight:300;font-size:10.4px;margin-top:8px}
</style>
</head>
<body>
<main class="sheet">

  <section class="label label--gold front" aria-label="Sauvignon Blanc front label">
    <div class="front__face">
      <div class="front__rule">
        <div class="brand"><span class="brand__dot"></span><span class="brand__name">BRINDOR RANCH</span></div>
        <div class="vineyard">Twelve Vines Vineyard</div>
        <div class="vintage">2022</div>
        <div class="variety">SAUVIGNON BLANC</div>
        <div class="appellation">California</div>
      </div>
      <div class="front__band">PALOS VERDES PENINSULA - NAPA VALLEY -</div>
    </div>
  </section>

  <section class="label label--silver front" aria-label="Cabernet Sauvignon front label">
    <div class="front__face">
      <div class="front__rule">
        <div class="brand"><span class="brand__dot"></span><span class="brand__name">BRINDOR RANCH</span></div>
        <div class="vineyard">Twelve Vines Vineyard</div>
        <div class="vintage">2022</div>
        <div class="variety">CABERNET SAUVIGNON</div>
        <div class="appellation">California</div>
      </div>
      <div class="front__band">PALOS VERDES PENINSULA - NAPA VALLEY -</div>
    </div>
  </section>

  <section class="label label--gold back" aria-label="Sauvignon Blanc back label">
    <div class="back__head">
      <div class="back__title">
        <div class="vineyard">Twelve Vines Vineyard</div>
        <div class="vintage">2022</div>
        <div class="variety">SAUVIGNON BLANC</div>
        <div class="appellation">California</div>
      </div>
      <div class="brand back__brand"><span class="brand__dot"></span><span class="brand__name">BRINDOR RANCH</span></div>
    </div>
    <div class="story">
      <p>Nestled between French lavender and roses, riding arenas and horse pastures, and the serenity of Rolling Hills lies Twelve Vines Vineyard. Established in 2014 at Liberty Acre Farm, a hobby farm owned by a mother and daughter, these 7 rows of Cabernet Sauvignon and 7 rows of Sauvignon Blanc are lovingly tended.</p>
      <p>The Sauvignon Blanc from the mist swept hill of the Palos Verdes Peninsula is sure to refresh any summer evening. Upon pouring a glass, you are greeted by waves of the aroma of citrus, infused with tropical flavors of luscious pineapple and guava. This light and crisp wine captures the coastal climate from which it was grown, perfectly suited for warm summer afternoons and al fresco dining.</p>
    </div>
    <div class="stars">★★★</div>
    <div class="producer">PRODUCED &amp; BOTTLED BY LIBERTY ACRE FARM, OAKHURST, CA</div>
    <div class="warning"><strong>Government Warning:</strong> (1) According to the Surgeon General, women should not drink alcoholic beverages during pregnancy because of the risk of birth defects. (2) Consumption of alcoholic beverages impairs your ability to drive a car or operate machinery, and may cause health problems.</div>
    <div class="facts"><span>CONTAINS SULFITES</span><span>ALC.12.5% BY VOL.</span><span>750 ML</span></div>
  </section>

  <section class="label label--silver back" aria-label="Cabernet Sauvignon back label">
    <div class="back__head">
      <div class="back__title">
        <div class="vineyard">Twelve Vines Vineyard</div>
        <div class="vintage">2022</div>
        <div class="variety">CABERNET SAUVIGNON</div>
        <div class="appellation">California</div>
      </div>
      <div class="brand back__brand"><span class="brand__dot"></span><span class="brand__name">BRINDOR RANCH</span></div>
    </div>
    <div class="story">
      <p>Nestled between French lavender and roses, riding arenas and horse pastures, and the serenity of Rolling Hills lies Twelve Vines Vineyard. Established in 2014 at Liberty Acre Farm, a hobby farm owned by a mother and daughter, these 7 rows of Cabernet Sauvignon and 7 rows of Sauvignon Blanc are lovingly tended.</p>
      <p>The Cabernet Sauvignon, grown from the limestone rich hills of the Palos Verdes Peninsula, is well balanced with light acidity. Richly flavored and garnet colored, with a delicately spiced aroma, this wine brings forth ripe red fruit flavors of blackberry and cherry. A prefect compliment to a hearty barbecued steak or pasta.</p>
    </div>
    <div class="stars">★★★</div>
    <div class="producer">PRODUCED &amp; BOTTLED BY LIBERTY ACRE FARM, OAKHURST, CA</div>
    <div class="warning"><strong>Government Warning:</strong> (1) According to the Surgeon General, women should not drink alcoholic beverages during pregnancy because of the risk of birth defects. (2) Consumption of alcoholic beverages impairs your ability to drive a car or operate machinery, and may cause health problems.</div>
    <div class="facts"><span>CONTAINS SULFITES</span><span>ALC.13.5% BY VOL.</span><span>750 ML</span></div>
  </section>

</main>
</body>
</html>
```